Monthly Mailed Newsletter/Magazine for Medical Spa

Every month we send out a mailed newsletter/magazine to our visitors from the previous month. We made a sample newsletter/magazine as a guideline of what we are looking for. We need a designer to make a simple and clean design layout.

- Attached is our sample design that has all the content we want to use.
- Newsletter/magazine is 8 pages total.
- Size of each page is 8.5 inches in width by 11 inches in height.
- Content and images can be located here: https://files.vornacloud.net/shared/8kqTRw3ZpLmX2vNcA7yHd5EbJ0sUgFo4e?view=open

The following will give you an idea of our brand presentation.
Our website is: www.GlowDermaClinic.com
Our Instagram; @glowdermaclinic
Our Facebook: www.socialtreo.com/glowdermaclinic

Target Market(s)

Women 25 - 45

Industry/Entity Type

Beauty

Font styles to use
Other font styles liked:
• Josefins Sans Bold & Lato

Colors
f78f20
ffffff

Requirements
Must have
• - Our Logo
- Our tagline: YOUR SKIN DESERVES IT!
- Address and contact information for our locations
- Our color scheme: Black and #FAA641
- Heading font is Josefin Sans Bold
- Paragraph font is Lato
- Our website address: www.GlowDermaClinic.com

```html
<!DOCTYPE html>
<html lang="en">
<head>
<meta charset="UTF-8">
<title>Glow Derma Clinic – Newsletter Spread</title>
<link href="https://fonts.googleapis.com/css2?family=Josefin+Sans:wght@400;700&family=Lato:wght@400;700&display=swap" rel="stylesheet">
<style>
  :root {
    --brand-orange: #faa641;
    --ink: #111111;
    --paper: #ffffff;
    --backdrop: #ececec;
    --body-text: #222222;
  }
  * { box-sizing: border-box; margin: 0; padding: 0; }
  html, body { width: 1200px; height: 671px; overflow: hidden; }
  body {
    background: var(--backdrop);
    position: relative;
    font-family: 'Lato', Arial, sans-serif;
    color: var(--ink);
  }
  .page {
    position: absolute;
    top: 31px;
    width: 470px;
    height: 608px;
    background: var(--paper);
    box-shadow: 0 4px 14px rgba(0,0,0,0.12);
    overflow: hidden;
  }
  .page--cover { left: 100px; }
  .page--article { left: 630px; }

  /* Cover */
  .cover__tab {
    position: absolute; left: 46px; top: 0;
    width: 153px; height: 53px;
    background: var(--brand-orange);
  }
  .brand {
    position: absolute; right: 62px; top: 48px;
    display: flex; flex-direction: column; align-items: flex-end; gap: 8px;
  }
  .brand__dot {
    width: 40px; height: 40px; border-radius: 50%;
    background: var(--brand-orange);
    margin-right: 62px;
  }
  .brand__name {
    font-family: 'Josefin Sans', Arial, sans-serif;
    font-weight: 700;
    font-size: 22px;
    color: var(--ink);
    letter-spacing: 0.5px;
  }
  .cover__photo {
    position: absolute; left: 26px; top: 199px;
    width: 417px; height: 244px;
    background: linear-gradient(120deg, #6b4a36 0%, #2a2322 30%, #c48a68 55%, #b83a2e 80%, #d9b8a3 100%);
  }
  .cover__overlap {
    position: absolute; left: 132px; top: 397px;
    width: 283px; height: 46px;
    background: var(--brand-orange);
    opacity: 0.55;
  }
  .tagline {
    position: absolute; left: 132px; top: 443px;
    width: 283px; height: 137px;
    background: var(--brand-orange);
    padding: 14px 0 0 33px;
    font-family: 'Josefin Sans', Arial, sans-serif;
    color: var(--ink);
    line-height: 1.05;
  }
  .tagline__light { font-weight: 400; font-size: 30px; }
  .tagline__bold { font-weight: 700; font-size: 36px; }
  .tagline__line { display: block; }

  /* Article */
  .article__title {
    position: absolute; left: 46px; top: 26px;
    font-family: 'Josefin Sans', Arial, sans-serif;
    font-size: 30px; line-height: 1.22;
    color: var(--ink);
  }
  .article__title-light { font-weight: 400; display: block; }
  .article__title-bold { font-weight: 700; display: block; }
  .article__photo {
    position: absolute; left: 45px; top: 133px;
    width: 281px; height: 168px;
    background: linear-gradient(135deg, #f2f2f2 0%, #d8d8d8 35%, #e6c4ad 55%, #f3f3f3 80%, #cfcfcf 100%);
  }
  .sidebar {
    position: absolute; left: 263px; top: 198px;
    width: 182px; height: 184px;
    background: var(--brand-orange);
    padding: 22px 14px 0 18px;
  }
  .sidebar__heading {
    font-family: 'Josefin Sans', Arial, sans-serif;
    font-weight: 700; font-size: 11px; line-height: 1.2;
    margin-bottom: 9px;
  }
  .sidebar__text { font-size: 9.6px; line-height: 1.38; color: var(--body-text); }
  .article__heading {
    position: absolute; left: 55px; top: 342px;
    font-family: 'Josefin Sans', Arial, sans-serif;
    font-weight: 700; font-size: 11px; line-height: 1.2;
  }
  .column {
    position: absolute;
    width: 188px;
    font-size: 7.1px; line-height: 1.36;
    color: var(--body-text);
    text-align: justify;
  }
  .column p { margin-bottom: 8px; }
  .column--left { left: 55px; top: 378px; }
  .column--right { left: 259px; top: 392px; }
  .article__block {
    position: absolute; left: 261px; top: 521px;
    width: 187px; height: 87px;
    background: var(--brand-orange);
  }
</style>
</head>
<body>

<section class="page page--cover">
  <div class="cover__tab"></div>
  <div class="brand">
    <div class="brand__dot"></div>
    <div class="brand__name">Glow Derma Clinic</div>
  </div>
  <div class="cover__photo" role="img" aria-label="Photo of a technician giving a laser hair removal treatment to a smiling client wearing protective glasses"></div>
  <div class="cover__overlap"></div>
  <div class="tagline">
    <span class="tagline__line"><span class="tagline__light">YOUR </span><span class="tagline__bold">SKIN</span></span>
    <span class="tagline__line tagline__bold">DESERVES</span>
    <span class="tagline__line tagline__light">IT!</span>
  </div>
</section>

<section class="page page--article">
  <h1 class="article__title">
    <span class="article__title-light">IS AT-HOME</span>
    <span class="article__title-bold">LASER HAIR REMOVAL</span>
    <span class="article__title-light">EFFECTIVE?</span>
  </h1>
  <div class="article__photo" role="img" aria-label="Photo of a handheld laser device being used on a leg resting on white sheets"></div>
  <aside class="sidebar">
    <h2 class="sidebar__heading">HOW DOES<br>LASER HAIR REMOVAL<br>WORK?</h2>
    <p class="sidebar__text">Laser hair removal uses a concentrated beam of light to target melanin, also known as your natural pigment. Through this, the follicle that produces hair is damaged. This delays the future growth of hairs.</p>
  </aside>
  <h2 class="article__heading">DO AT-HOME LASER HAIR<br>REMOVAL GADGETS WORK?</h2>
  <div class="column column--left">
    <p>NYC's dermatology professionals answer the million-dollar question with a very cautionary yes. Dr. Lena Marwick claims that results vary according to individuals. Success is dependent on the contrast between your hair and skin color. Light skin and dark hair produce the best outcomes, while other combinations can prove them ineffective. Generally, athome products are more suitable for use on smaller areas such as your lip and underarms. They can also be beneficial for maintenance after in-office treatments</p>
    <p>deadline environment means that copy editing often takes the form of deleting everything past an arbitrary point in the story corresponding to the dictates of available space on a page.</p>
    <p>Therefore, newspaper reporters are trained to write in inverted pyramid style, with all the most important information in the first paragraph or</p>
  </div>
  <div class="column column--right">
    <p>two. If the less vital details are pushed towards the end of the story, then the potentially destructive impact of draconian copy editing will be minimized.</p>
    <p>A news article can include accounts of eyewitnesses to the happening event. It can contain photographs, accounts, statistics, graphs, recollections, interviews, polls, debates on the topic, etc.<br>Quoted references can also be helpful. References to people can also be made through the written.</p>
  </div>
  <div class="article__block"></div>
</section>

</body>
</html>
```